Attract renters to our neighborhoods - inform renters who we are

Apartments in several neighborhoods. We want to attract renters who want to live along the lake or other near by neighborhoods. We want them to know that we have an apartment for them in their location.
The perfect location to spend your time.
When minutes matter LIVE where you work and play! (love this tag line)
Updates

www.kvtresidences.example Choose from over 3,700 apartments in Chicago’s most celebrated neighborhoods. 773-582-6041 Chicago’s most celebrated neighborhoods. 31 PROPERTIES

Target Market(s)

Sophisticated apartment renter who wants location, space, amenities

Industry/Entity Type

Apartment Rentals

Requirements
Must have
• Feel like I want to live there, or the ad is calling me
Nice to have
• Appeal to a sophisticated apartment renter. We have what you want, where you want to be.
Should not have
• Logo colors are black and red/burnt orange see attached logo

```html
<!DOCTYPE html>
<html lang="en">
<head>
<meta charset="UTF-8">
<title>KVT Residences – Apartment Flyer</title>
<link href="https://fonts.googleapis.com/css2?family=Montserrat:wght@500;600;700;800&family=Oswald:wght@500;600&display=swap" rel="stylesheet">
<style>
  :root {
    --red: #b5212b;
    --charcoal: #2b2e33;
    --ink: #111111;
    --white: #ffffff;
    --badge-grey: #a7a9ac;
    --lake: #3aa7a6;
    --lake-deep: #1f7f86;
    --sky: #dfe9ee;
    --city: #7d8a80;
    --stage: #e6e6e6;
  }
  * { box-sizing: border-box; margin: 0; padding: 0; }
  html, body { width: 1200px; height: 800px; overflow: hidden; }
  body {
    background: var(--stage);
    font-family: "Montserrat", Arial, sans-serif;
    position: relative;
  }
  .flyer {
    position: absolute;
    left: 330px; top: 20px;
    width: 540px; height: 760px;
    background: var(--white);
    overflow: hidden;
    box-shadow: 0 4px 18px rgba(0,0,0,.18);
  }
  .hero {
    position: absolute; left: 0; top: 150px; width: 540px; height: 320px;
    background:
      linear-gradient(180deg, var(--sky) 0%, #a9bbbd 16%, var(--city) 38%, #6c8a62 56%, var(--lake) 72%, var(--lake-deep) 100%);
  }
  .tagline {
    position: absolute; right: 0; top: 22px;
    width: 330px; height: 84px;
    background: var(--red);
    color: var(--white);
    font-weight: 700; font-size: 20px; line-height: 1.3;
    padding: 15px 18px 0 22px;
    white-space: nowrap;
  }
  .brand {
    position: absolute; left: 28px; top: 114px;
    display: flex; align-items: center; gap: 10px;
  }
  .brand-square { width: 20px; height: 20px; background: var(--red); }
  .brand-name {
    font-weight: 800; font-size: 20px; color: var(--ink); letter-spacing: .5px;
    white-space: nowrap;
  }
  .headline {
    position: absolute; left: 28px; top: 380px; width: 330px;
    color: var(--white); font-weight: 600; font-size: 19px; line-height: 1.3;
    text-shadow: 0 1px 3px rgba(0,0,0,.35);
  }
  .headline strong { font-weight: 800; }
  .panel {
    position: absolute; left: 0; top: 470px; width: 540px; height: 178px;
    background: var(--charcoal);
  }
  .seal {
    position: absolute; left: 378px; top: 338px; width: 142px; height: 142px;
  }
  .seal-text {
    position: absolute; left: 378px; top: 338px; width: 142px; height: 142px;
    display: flex; flex-direction: column; align-items: center; justify-content: center;
    color: var(--white); text-align: center;
    font-family: "Oswald", Arial, sans-serif;
  }
  .seal-text .small { font-size: 10.5px; font-weight: 500; line-height: 1.25; letter-spacing: .3px; }
  .seal-text .rule { width: 62px; height: 1px; background: rgba(255,255,255,.6); margin: 6px 0; }
  .seal-text .big { font-size: 17px; font-weight: 600; }
  .hoods {
    position: absolute; left: 16px; top: 488px; width: 508px;
    display: grid; grid-template-columns: repeat(4, 1fr); gap: 10px;
  }
  .hood-photo { height: 88px; }
  .hood-photo.gold { background: linear-gradient(160deg, #b9d3e2, #6f7f86 55%, #3c8f9a); }
  .hood-photo.river { background: linear-gradient(160deg, #c6dbe6, #84908f 50%, #5d6b63); }
  .hood-photo.lincoln { background: linear-gradient(160deg, #c2d7df, #7b8b70 45%, #e0cfa9 62%, #2e9aa0); }
  .hood-photo.lake { background: linear-gradient(160deg, #bfd2db, #8d9890 45%, #5d8a5a 62%, #2f8e97); }
  .hood-name {
    color: var(--white); font-weight: 700; font-size: 12.5px; margin-top: 10px; line-height: 1.25;
  }
  .hood-name::after {
    content: ""; display: block; width: 30px; height: 3px; background: var(--red); margin-top: 6px;
  }
  .partners {
    position: absolute; left: 0; top: 648px; width: 540px; height: 60px;
    display: flex; justify-content: space-around; align-items: center; padding: 0 20px;
  }
  .partner { background: var(--badge-grey); }
  .partner.wide { width: 52px; height: 26px; border-radius: 2px; }
  .partner.square { width: 30px; height: 30px; }
  .partner.round { width: 30px; height: 30px; border-radius: 50%; }
  .contact {
    position: absolute; left: 0; bottom: 0; width: 540px; height: 52px;
    background: var(--red); color: var(--white);
    display: flex; align-items: center; justify-content: space-between;
    padding: 0 14px;
    font-weight: 700; font-size: 9px; white-space: nowrap;
  }
  .contact-item { display: flex; align-items: center; gap: 5px; }
  .contact-item .value { font-weight: 600; font-size: 9.5px; }
  .contact-divider { width: 1px; height: 24px; background: rgba(255,255,255,.55); }
  .icon { width: 14px; height: 14px; flex: none; }
</style>
</head>
<body>
  <div class="flyer">
    <div class="hero" role="img" aria-label="Aerial photograph of the Chicago skyline, lakefront park, harbor and turquoise lake"></div>

    <div class="tagline">When minutes matter LIVE<br>where you work and play!</div>

    <div class="brand">
      <span class="brand-square"></span>
      <span class="brand-name">KVT RESIDENCES</span>
    </div>

    <div class="panel"></div>

    <p class="headline">Choose from over <strong>3,700</strong> apartments in Chicago’s most celebrated neighborhoods.</p>

    <svg class="seal" viewBox="0 0 142 142" aria-hidden="true">
      <circle cx="71" cy="71" r="70" fill="#ffffff"/>
      <circle cx="71" cy="71" r="63" fill="var(--red)"/>
      <circle cx="71" cy="71" r="55" fill="var(--charcoal)"/>
      <circle cx="71" cy="71" r="50" fill="none" stroke="var(--red)" stroke-width="1" stroke-dasharray="3 3"/>
    </svg>
    <div class="seal-text">
      <span class="small">CHICAGO’S<br>MOST CELEBRATED<br>NEIGHBORHOODS.</span>
      <span class="rule"></span>
      <span class="big">31 PROPERTIES</span>
    </div>

    <div class="hoods">
      <div class="hood">
        <div class="hood-photo gold" role="img" aria-label="Aerial view of Gold Coast and Old Town towers by the lake"></div>
        <p class="hood-name">Gold Coast &amp; Old Town</p>
      </div>
      <div class="hood">
        <div class="hood-photo river" role="img" aria-label="Aerial view of River North high-rises"></div>
        <p class="hood-name">River North</p>
      </div>
      <div class="hood">
        <div class="hood-photo lincoln" role="img" aria-label="Aerial view of Lincoln Park beach and shoreline"></div>
        <p class="hood-name">Lincoln Park</p>
      </div>
      <div class="hood">
        <div class="hood-photo lake" role="img" aria-label="Aerial view of Lakeview harbor and park"></div>
        <p class="hood-name">Lakeview</p>
      </div>
    </div>

    <div class="partners" aria-label="Partner and certification badges">
      <span class="partner wide"></span>
      <span class="partner wide"></span>
      <span class="partner square"></span>
      <span class="partner round"></span>
      <span class="partner square"></span>
      <span class="partner wide"></span>
      <span class="partner square"></span>
    </div>

    <div class="contact">
      <div class="contact-item">
        <span>CALL US TODAY</span>
        <svg class="icon" viewBox="0 0 16 16" aria-hidden="true">
          <circle cx="8" cy="8" r="7.2" fill="none" stroke="#fff" stroke-width="1.2"/>
          <path d="M5.3 4.3l1.4-.3.8 1.9-.9.7a5 5 0 0 0 2.3 2.3l.7-.9 1.9.8-.3 1.4c-3.2.3-6.2-2.7-5.9-5.9z" fill="#fff"/>
        </svg>
        <span class="value">773-582-6041</span>
      </div>
      <span class="contact-divider"></span>
      <div class="contact-item">
        <span>FOR MORE INFORMATION</span>
        <svg class="icon" viewBox="0 0 16 16" aria-hidden="true">
          <circle cx="8" cy="8" r="7.2" fill="none" stroke="#fff" stroke-width="1.2"/>
          <circle cx="8" cy="8" r="4.2" fill="none" stroke="#fff" stroke-width="1"/>
          <ellipse cx="8" cy="8" rx="1.8" ry="4.2" fill="none" stroke="#fff" stroke-width="1"/>
          <line x1="3.8" y1="8" x2="12.2" y2="8" stroke="#fff" stroke-width="1"/>
        </svg>
        <span class="value">www.kvtresidences.example</span>
      </div>
    </div>
  </div>
</body>
</html>
```